Aunt Rolina's Bakery

I am about to create a luxury boutique that specializes in cake baking and cupcake
and ready for parties and special events and order delivery
the logo has already made

Industry/Entity Type

Boutique

Contact Information for Business Card

Email:auntrolinasbakery@maplecrumbmail.com
Instagram: aunt_rolina_bakery
Twitter: xxxxxxx
WhatsApp: xxxxxxx

Requirements
Must have
• luxury design

```html
<!DOCTYPE html>
<html lang="en">
<head>
<meta charset="utf-8">
<title>Aunt Rolina's Bakery – Business Card</title>
<link rel="stylesheet" href="https://fonts.googleapis.com/css2?family=Kanit:wght@300&display=swap">
<style>
  :root {
    --backdrop: #ececec;
    --card: #ffffff;
    --rose: #dd9fad;
    --taupe: #7c7873;
    --ink-light: #ffffff;
    --logo-grey: #86817c;
  }
  * { box-sizing: border-box; margin: 0; padding: 0; }
  html, body {
    width: 1200px; height: 799px; overflow: hidden;
    background: var(--backdrop);
    font-family: "Kanit", sans-serif;
    font-weight: 300;
  }
  .business-card {
    position: absolute;
    left: 160px; top: 153px;
    width: 880px; height: 492px;
    background: var(--card);
    box-shadow: 0 6px 18px rgba(0,0,0,0.12);
    overflow: hidden;
  }
  .card-wave { position: absolute; inset: 0; width: 880px; height: 492px; }
  .contact-list {
    position: absolute;
    left: 50px; top: 282px;
    list-style: none;
    color: var(--ink-light);
    font-size: 17px;
    line-height: 35px;
    white-space: nowrap;
  }
  .contact-item { display: flex; align-items: center; gap: 10px; }
  .contact-dot {
    width: 18px; height: 18px; border-radius: 50%;
    background: var(--ink-light); flex: none;
  }
  .contact-icon { width: 18px; height: 13px; flex: none; }
  .brand-lockup {
    position: absolute;
    left: 436px; top: 0; width: 340px; height: 492px;
    display: flex; flex-direction: column; align-items: center;
    padding-top: 58px;
    gap: 26px;
  }
  .brand-mark {
    width: 104px; height: 104px; border-radius: 50%;
    background: var(--rose);
    border: 6px solid var(--logo-grey);
    flex: none;
  }
  .brand-name {
    color: var(--logo-grey);
    font-size: 40px;
    letter-spacing: 1px;
    text-align: center;
    line-height: 1.15;
  }
</style>
</head>
<body>
  <main class="business-card">
    <svg class="card-wave" viewBox="0 0 880 492" aria-hidden="true">
      <path d="M376 0 C350 60 320 130 340 200 C360 280 430 400 511 492 H0 V0 Z" fill="var(--rose)"/>
      <path d="M376 0 C350 60 320 130 340 200 C360 280 430 400 511 492" fill="none" stroke="var(--taupe)" stroke-width="7"/>
    </svg>

    <ul class="contact-list">
      <li class="contact-item"><span class="contact-dot"></span>xxxxxxxxxxxx</li>
      <li class="contact-item"><span class="contact-dot"></span>xxxxxxxxxxxx</li>
      <li class="contact-item"><span class="contact-dot"></span>aunt_rolina_bakery</li>
      <li class="contact-item">
        <svg class="contact-icon" viewBox="0 0 22 16" aria-hidden="true">
          <rect x="1" y="1" width="20" height="14" fill="none" stroke="#fff" stroke-width="1.5"/>
          <path d="M1 1 L11 9 L21 1" fill="none" stroke="#fff" stroke-width="1.5"/>
        </svg>
        auntrolinasbakery@maplecrumbmail.com
      </li>
    </ul>

    <div class="brand-lockup">
      <span class="brand-mark"></span>
      <p class="brand-name">Aunt Rolina's<br>Bakery</p>
    </div>
  </main>
</body>
</html>
```